Brochure for College Student Program at Local Family Doctor office

I am a family doctor that offers a program for local college students, who are from out of state, a way to have a local...well, family doctor near their school. My website is www.maplewynddpc.com and there is a section on college students that explains this is more detail. This brochure (double side) tri-fold will be going to parents so it is made for them. It has to give the feeling of peace of mind, of security that their kids are in good hands, etc. I want to use the colors of the logo. The pictures on the website should be used including the two pictures of me and the logo. Any other pictures can be used as well and I can send then in bigger sizes if you want. Basically all the information is on that section of the site BUT you may need to add other parts as well like our hours, our services, stuff about me, etc. All that is on the site. I added some below.

Target Market(s)

College students' Parents

Industry/Entity Type

College

Requirements
Must have
• My picture (on website) - use both on website
• Our colors and logo
• Other pictures on website
• Office (555) 382-7190
• Fax (555) 941-6073
• 2875 Harlow Bend Ln., Suite C.
• Forest, VA 24551 (Kestrel Medical Commons off Tamber Rd, across from Pillbrook)
• Office Hourse: M-F from 9 to 5
• Maplewynd Direct Primary Care is enhanced and personalized healthcare without the interference of insurance companies. For a small fee per semester your child gets to have his or her own local doctor right in town.
• Look at the college student section on the site and get most if not all of that on there.
• Only 200 students are accepted each year and it is on a first come, first serve basis. Join your child online now!
Nice to have
• I think I would like a white brochure but the blue and green colores but open to options
• Dr. Bernard Quellin has 20 years of experience in family medicine, sports medicine, nutrition, exercise and osteopathic manipulation. He is the inventor of the Joint Mender and the ChillCap. He has been featured in the Tri-County Ledger, the Unified Newswire, the National Weekly Digest and Review, WBX and more. He will be your doctor when you join Maplewynd Direct Primary Care. No one else.
• As a member of the Maplewynd DPC, you’ll have access to the following:
• 1. Increased access to your doctor for your child. After hours, weekends, holidays – you have the ability to receive excellent medical care.
• 2. Extended, relaxed visits. Your child will not feel rushed through an appointment, and there’s never a question he or she won’t have time to ask.
• 3. Because we accept less patients, your chiold will have a real relationship with his or her doctor.
• 4. Full access via technology. Your child will be able to reach the doctor and other medical information via e-mail, text, cell phone and more. The sky is the limit.
• 5. Osteopathic Manipulation Treatment (OMT) – Dr. Quellin is one of the few MDs in the country who performs OMT on a regular basis. Since his training in residency he as treated over 15,000 patients using this technique.
• 6. Diagnostic and procedural benefits at no extra costs (see below).
• 7. Wholesale labs done right in the office. We’ll pass our benefits right on down to you and your child.
• List of Covered Services
• Comprehensive Physical
• Sports/School Physicals
• Preventive Care
• Management of Chronic Illness
• Dietary/Nutritional Counseling
• Exercise Recommendations
• Osteopathic Manipulation (Back Treatment)
• Laceration Repair
• Cryotherapy
• Skin Biopsies
• Need for Urgent Care Visits
• Mole Removals
• EKG
• Acute Visits
• Joint Injections
• Nebulizer Treatments
• House Calls
• Email, Text Questions
• Blood Draws
• List of Uncovered Services
• Immunizations
• Hospitalizations
• Pathology Fees
• Specialist Care
• Lab Work (they are discounted very heavily, however. Some up to 90%!)
• Physical Therapy
• Surgical Procedures
• ER visits
• Radiological Studies

```html
<!DOCTYPE html>
<html lang="en">
<head>
<meta charset="utf-8">
<title>Maplewynd Direct Primary Care – College Student Brochure</title>
<link rel="stylesheet" href="https://fonts.googleapis.com/css2?family=Montserrat:wght@200;300&family=Arimo:wght@400&display=swap">
<style>
  :root {
    --navy: #1d2b5c;
    --ink: #1f1f1f;
    --sky-pale: #eef4fa;
    --sky-light: #d3e3f1;
    --sky-mid: #9fbfdc;
    --steel: #5c83ad;
    --brick: #a0523c;
    --leaf: #2f8a3e;
    --sun-faint: #fbf3d6;
    --page: #ffffff;
  }
  * { box-sizing: border-box; margin: 0; padding: 0; }
  html, body { width: 1200px; height: 927px; overflow: hidden; background: var(--page); }
  body { position: relative; font-family: "Arimo", Arial, sans-serif; color: var(--ink); }

  .brochure {
    position: absolute; left: 62px; top: 47px; width: 1078px; height: 831px;
    display: flex; background: var(--page);
    box-shadow: 0 4px 14px rgba(0,0,0,.35);
    overflow: hidden;
  }
  .panel { position: relative; width: 359px; height: 100%; overflow: hidden; }

  .display { font-family: "Montserrat", sans-serif; font-weight: 200; color: var(--navy); line-height: .95; text-transform: uppercase; }
  .body-copy { font-size: 13.4px; line-height: 18.9px; letter-spacing: -0.3px; }

  /* Intro panel */
  .panel--intro { background: linear-gradient(180deg, var(--page) 0%, var(--sky-pale) 40%, var(--sky-light) 70%, var(--sky-mid) 100%); }
  .intro-headline { position: absolute; left: 30px; top: 30px; }
  .intro-headline .big { font-size: 66px; letter-spacing: 1px; display: block; }
  .intro-headline .sub { font-size: 37px; display: block; letter-spacing: .5px; margin-top: 6px; line-height: 1; }
  .intro-copy { position: absolute; left: 34px; top: 253px; width: 296px; }
  .intro-copy p + p { margin-top: 18.9px; }
  .brand-mark { position: absolute; left: 96px; top: 470px; display: flex; align-items: center; gap: 8px; z-index: 1; }
  .brand-mark .dot { width: 12px; height: 12px; border-radius: 50%; background: var(--leaf); }
  .brand-mark .name { font-size: 12.5px; line-height: 15px; color: var(--navy); width: 140px; text-align: center; }
  .photo-mascot {
    position: absolute; left: 0; top: 560px; width: 359px; height: 271px;
    background: radial-gradient(ellipse at 55% 65%, #8a6a4c 0%, #6f8fae 45%, rgba(169,195,220,0) 85%);
  }

  /* Access panel */
  .panel--access { background: var(--page); }
  .photo-instrument {
    position: absolute; left: 0; top: 0; width: 359px; height: 226px;
    background: radial-gradient(ellipse at 55% 45%, var(--steel) 0%, var(--sky-light) 55%, var(--page) 100%);
  }
  .access-lead { position: absolute; left: 24px; top: 252px; font-size: 13.4px; letter-spacing: -0.3px; }
  .access-title { position: absolute; left: 20px; top: 267px; font-size: 58px; letter-spacing: -1.5px; }
  .access-list { position: absolute; left: 24px; top: 326px; width: 318px; list-style: none; }
  .access-list li + li { margin-top: 18.9px; }

  /* Services panel */
  .panel--services { background: var(--page); }
  .chevron { position: absolute; right: -40px; top: 150px; }
  .services-kicker { position: absolute; left: 24px; top: 31px; font-family: "Montserrat", sans-serif; font-weight: 300; font-size: 19px; color: var(--navy); letter-spacing: 1px; }
  .services-title { position: absolute; left: 20px; top: 50px; font-size: 64px; letter-spacing: -.5px; }
  .service-list { list-style: none; font-size: 13.6px; line-height: 18.9px; letter-spacing: -0.2px; }
  .service-list--covered { position: absolute; left: 24px; top: 116px; }
  .uncovered-title { position: absolute; left: 29px; top: 488px; font-family: "Montserrat", sans-serif; font-weight: 300; font-size: 19px; color: var(--navy); line-height: 22px; }
  .service-list--uncovered { position: absolute; left: 24px; top: 510px; }
  .note { font-size: 10.5px; }
  .photo-office {
    position: absolute; left: 0; top: 668px; width: 359px; height: 163px;
    background: linear-gradient(180deg, rgba(223,233,243,0) 0%, #c9d3dc 22%, var(--brick) 50%, #8a8f94 78%, #b9bdc0 100%);
  }
</style>
</head>
<body>
  <main class="brochure">
    <section class="panel panel--intro">
      <h1 class="intro-headline display">
        <span class="big">Your</span>
        <span class="big">Own</span>
        <span class="sub">Personalized</span>
        <span class="sub">Healthcare</span>
      </h1>
      <div class="intro-copy body-copy">
        <p>Maplewynd Direct Primary Care is enhanced and personalized healthcare without the interference of insurance companies. For a small fee per semester your child gets to have his or her own local doctor right in town. Look at the college student section on the site and get most if not all of that on there.</p>
        <p>Only 200 students are accepted each year and it is on a first come, first serve basis. Join your child online now!</p>
      </div>
      <div class="brand-mark">
        <span class="dot"></span>
        <span class="name">Maplewynd Direct Primary Care</span>
      </div>
      <div class="photo-mascot" role="img" aria-label="Photo of a teddy bear dressed in surgical scrubs beside medical books"></div>
    </section>

    <section class="panel panel--access">
      <div class="photo-instrument" role="img" aria-label="Photo of a stethoscope on a bright white background"></div>
      <p class="access-lead">As a member of the Maplewynd DPC, you’ll have</p>
      <h2 class="access-title display">Access to:</h2>
      <ol class="access-list body-copy">
        <li>1. Increased access to your doctor for your child. After hours, weekends, holidays – you have the ability to receive excellent medical care.</li>
        <li>2. Extended, relaxed visits. Your child will not feel rushed through an appointment, and there’s never a question he or she won’t have time to ask.</li>
        <li>3. Because we accept less patients, your chiold will have a real relationship with his or her doctor.</li>
        <li>4. Full access via technology. Your child will be able to reach the doctor and other medical information via e-mail, text, cell phone and more. The sky is the limit.</li>
        <li>5. Osteopathic Manipulation Treatment (OMT) – Dr. Quellin is one of the few MDs in the country who performs OMT on a regular basis. Since his training in residency he as treated over 15,000 patients using this technique.</li>
        <li>6. Diagnostic and procedural benefits at no extra costs (see below).</li>
        <li>7. Wholesale labs done right in the office. We’ll pass our benefits right on down to you and your child.</li>
      </ol>
    </section>

    <section class="panel panel--services">
      <svg class="chevron" width="160" height="260" viewBox="0 0 160 260" aria-hidden="true">
        <polygon points="160,0 160,70 80,130 160,190 160,260 10,130" fill="var(--sun-faint)"/>
      </svg>
      <p class="services-kicker">COVERED</p>
      <h2 class="services-title display">Services</h2>
      <ul class="service-list service-list--covered">
        <li>- Comprehensive Physical</li>
        <li>- Sports/School Physicals</li>
        <li>- Preventive Care</li>
        <li>- Management of Chronic Illness</li>
        <li>- Dietary/Nutritional Counseling</li>
        <li>- Exercise Recommendations</li>
        <li>- Osteopathic Manipulation (Back Treatment)</li>
        <li>- Laceration Repair</li>
        <li>- Cryotherapy</li>
        <li>- Skin Biopsies</li>
        <li>- Need for Urgent Care Visits</li>
        <li>- Mole Removals</li>
        <li>- EKG</li>
        <li>- Acute Visits</li>
        <li>- Joint Injections</li>
        <li>- Nebulizer Treatments</li>
        <li>- House Calls</li>
        <li>- Email, Text Questions</li>
        <li>- Blood Draws</li>
      </ul>
      <h3 class="uncovered-title">UNCOVERED SERVICES</h3>
      <ul class="service-list service-list--uncovered">
        <li>- Immunizations</li>
        <li>- ER visits or Hospitalizations</li>
        <li>- Pathology Fees</li>
        <li>- Specialist Care</li>
        <li>- Lab Work <span class="note">(discounted very heavily, Some up to 90%)</span></li>
        <li>- Physical Therapy</li>
        <li>- Surgical Procedures</li>
        <li>- Radiological Studies</li>
      </ul>
      <div class="photo-office" role="img" aria-label="Photo of the brick office building with its parking lot"></div>
    </section>
  </main>
</body>
</html>
```